I am looking for help designing my new business cards. I would like rounded edges and a raised logo on the back of the card. I have 2 Logos. One with a boat in it and one without. I'd like the one on the back to be the one that includes the boat and just the name on the front. I have included multiple formats of my logo. Please let me know if you need anymore.

Target Market(s)

Potential buyers and other sales brokers

Industry/Entity Type

Sales - Yacht / Boat Sales

Contact Information for Business Card

Id liike the front to include just the business name portion of the logo along with my name (Corwin Dalby), phone number (555.318.6027), website address (www.dalbymarineco.example) and not my physical address but just "Port Wellmont, SC". The back should include my full logo that has the boat included. This portion I'd prefer raised amd take up the majority of the space there. Thanks!!

Colors
0054AA
0677BA
7BADD7
CADEEF
E8F1F8
0094D4
00A9DD
6FCCEA
C7EBF8
E9F6FB

Requirements
Must have
• Double sided
Nice to have
• My email address: Corwin@dalbymarineco.example The NMTG logo somewhere small on the front of the card
Should not have
• My full address, prefer only "Port Wellmont, SC"

```html
<!DOCTYPE html>
<html lang="en">
<head>
<meta charset="utf-8">
<title>Dalby Marine Co — Business Card</title>
<link href="https://fonts.googleapis.com/css2?family=Poppins:wght@400;700;800&display=swap" rel="stylesheet">
<style>
  :root {
    --backdrop: #b3c3d2;
    --navy: #273a6e;
    --ocean: #1f88c6;
    --mist: #cde9f5;
    --mist-deep: #a9d8ee;
    --white: #ffffff;
  }
  * { box-sizing: border-box; margin: 0; padding: 0; }
  html, body {
    width: 1200px; height: 1200px; overflow: hidden;
    background: var(--backdrop);
    font-family: "Poppins", sans-serif;
  }
  .card {
    position: absolute;
    left: 190px;
    width: 820px; height: 480px;
    border-radius: 44px;
    overflow: hidden;
    box-shadow: 0 18px 40px rgba(40, 60, 90, 0.25);
  }
  .card--back { top: 90px; background: var(--ocean); }
  .card--front { top: 630px; background: var(--ocean); }

  /* Back side */
  .back-panel {
    position: absolute; inset: 0;
    background: var(--mist);
    clip-path: polygon(19% 0, 100% 0, 100% 100%, 20% 100%);
  }
  .boat-illustration {
    position: absolute;
    left: 200px; top: 70px;
    width: 560px; height: 220px;
    border-radius: 110px 24px 24px 110px;
    background: linear-gradient(100deg, var(--mist-deep) 0%, #7fb9e0 55%, var(--mist-deep) 100%);
    opacity: 0.85;
  }
  .back-wordmark {
    position: absolute;
    left: 200px; right: 40px; top: 300px;
    text-align: center;
    color: var(--navy);
    font-weight: 800;
    font-size: 70px;
    line-height: 1.1;
    letter-spacing: 2px;
    text-transform: uppercase;
  }

  /* Front side */
  .front-panel {
    position: absolute; inset: 0;
    background: var(--mist);
    clip-path: polygon(0 0, 32% 0, 42% 100%, 0 100%);
  }
  .front-wordmark {
    position: absolute;
    left: 90px; top: 240px;
    transform: translate(-50%, -50%) rotate(-90deg);
    white-space: nowrap;
    color: var(--navy);
    font-weight: 800;
    font-size: 44px;
    letter-spacing: 1px;
    text-transform: uppercase;
  }
  .contact {
    position: absolute;
    right: 70px; top: 70px;
    text-align: right;
    color: var(--white);
  }
  .contact__name {
    font-weight: 700;
    font-size: 30px;
    margin-bottom: 70px;
  }
  .contact__line {
    font-weight: 400;
    font-size: 25px;
    line-height: 1.3;
  }
</style>
</head>
<body>
  <section class="card card--back" aria-label="Card back">
    <div class="back-panel"></div>
    <div class="boat-illustration" role="img" aria-label="Line illustration of a centre-console fishing boat cutting through a blue wave"></div>
    <div class="back-wordmark">Dalby Marine Co</div>
  </section>

  <section class="card card--front" aria-label="Card front">
    <div class="front-panel"></div>
    <div class="front-wordmark">Dalby Marine Co</div>
    <div class="contact">
      <p class="contact__name">Corwin Dalby</p>
      <p class="contact__line">555.318.6027</p>
      <p class="contact__line">www.dalbymarineco.example</p>
      <p class="contact__line">Port Wellmont, SC</p>
    </div>
  </section>
</body>
</html>
```